Invitation Design Project

I would like to have a custom invitation (and reception/response cards) designed for my son's Bar Mitzvah. I have a strong idea of what I want and have a few mock-ups, but my "home made" effort would be improved by the addition of professional creativity and skill. The invitation should be white, red, and black, and a bold typographic style (see attachment). I am looking for a clean modern feel, and prefer square shaped invitations. I need the final product in an electronic format that I could either print myself or have done at a local printer.

Target Market(s)

Guests to a Bar Mitzvah. A group of family and friends ranging from 40-60 years of age, and a group of my son's 13 year old friends.

Industry/Entity Type

Electronic

Requirements
Must have
• Square shaped invitation (exact dimensions in attached file)
Typographic style
Red, black, white
Red color should be CMYK: 30-96-76-26
Nice to have
• I like the two icons on my attached sample reception card, especially the swirl/Torah one. I would be nice to use these (or similar ones) if there is a way to do so, but this is not a requirement.

```html
<!DOCTYPE html>
<html lang="en">
<head>
<meta charset="utf-8">
<title>Ethan's Bar Mitzvah Invitation Suite</title>
<link rel="stylesheet" href="https://fonts.googleapis.com/css2?family=Quicksand:wght@300;400;500&family=Fira+Sans+Condensed:wght@300;400&family=Oswald:wght@500&display=swap">
<style>
  :root {
    --red: #c8102e;
    --ink: #1a1a1a;
    --paper: #ffffff;
  }
  * { box-sizing: border-box; margin: 0; padding: 0; }
  html, body { width: 1200px; height: 600px; overflow: hidden; background: var(--paper); }
  .canvas {
    position: relative; width: 1200px; height: 600px; overflow: hidden;
    background: var(--paper); color: var(--ink);
    font-family: "Quicksand", sans-serif; font-weight: 400;
  }
  .card { position: absolute; border: 5px solid var(--red); background: var(--paper); }
  .justify { text-align: justify; text-align-last: justify; white-space: nowrap; }
  .outline-word { position: absolute; overflow: visible; }
  .outline-word text {
    font-family: "Oswald", sans-serif; font-weight: 500;
    fill: var(--paper); stroke: var(--red); stroke-width: 2.2; paint-order: normal;
  }

  /* RSVP card */
  .rsvp-card { left: 167px; top: 35px; width: 266px; height: 265px; overflow: visible; }
  .rsvp-card .outline-word { left: 0; top: -5px; }
  .rsvp-deadline { position: absolute; left: 10px; width: 236px; text-align: center; }
  .rsvp-deadline .date-line { font-size: 12px; letter-spacing: 0.3px; top: 64px; position: absolute; left: 0; width: 236px; }
  .rsvp-deadline .year-line { font-size: 15.5px; letter-spacing: 1.2px; top: 82px; position: absolute; left: 0; width: 236px; }
  .rsvp-options { position: absolute; top: 156px; left: 26px; display: flex; gap: 0; }
  .rsvp-option { display: flex; align-items: center; gap: 6px; font-size: 12.5px; letter-spacing: 0.4px; width: 114px; }
  .rsvp-box { width: 23px; height: 23px; border: 2.5px solid var(--red); }
  .rsvp-names { position: absolute; top: 210px; left: 25px; display: flex; align-items: center; font-size: 11.5px; letter-spacing: 0.4px; }
  .rsvp-names svg { margin-left: 4px; }

  /* Reception card */
  .reception-card { left: 167px; top: 315px; width: 266px; height: 266px; overflow: visible; }
  .reception-text { position: absolute; left: 0; width: 256px; text-align: center; }
  .reception-invite { top: 52px; font-size: 13px; line-height: 18px; letter-spacing: 1.6px; }
  .reception-invite .lower { letter-spacing: 1.3px; }
  .reception-venue { top: 123px; font-size: 14px; line-height: 18.5px; letter-spacing: 1.2px; }
  .reception-venue .venue-name { letter-spacing: 1.6px; }
  .reception-card .outline-word { left: 4px; bottom: -9px; }

  /* Main invitation */
  .invitation-card { left: 602px; top: 3px; width: 595px; height: 594px; border-width: 6px; }
  .intro { position: absolute; left: 41px; top: 58px; width: 500px; font-size: 23px; line-height: 28px; letter-spacing: 1px; }
  .invitation-card .outline-word { left: 41px; top: 131px; }
  .occasion {
    position: absolute; left: 41px; top: 256px; width: 502px;
    font-family: "Fira Sans Condensed", sans-serif; font-weight: 300;
    font-size: 37px; line-height: 40px; color: var(--red); letter-spacing: 0.2px;
  }
  .date-block { position: absolute; left: 41px; top: 326px; width: 194px; }
  .date-block .weekday { font-size: 35px; line-height: 36px; letter-spacing: 1.5px; }
  .date-block .small { font-size: 12.5px; line-height: 20px; letter-spacing: 0.6px; }
  .date-block .time { display: flex; align-items: flex-end; margin-top: 0; }
  .date-block .time-num { font-size: 43px; line-height: 40px; letter-spacing: 1px; }
  .date-block .time-note { font-size: 14px; line-height: 15px; letter-spacing: 0.8px; margin-left: 2px; padding-bottom: 3px; }
  .venue-block { position: absolute; left: 288px; top: 330px; width: 244px; }
  .venue-block .small { font-size: 16px; line-height: 22px; letter-spacing: 0.8px; }
  .venue-block .large { font-size: 31px; line-height: 34px; letter-spacing: 1.2px; }
  .venue-block .gap { margin-top: 4px; }
  .kiddush {
    position: absolute; left: 41px; top: 488px; width: 502px;
    font-family: "Fira Sans Condensed", sans-serif; font-weight: 400;
    font-size: 15.5px; color: var(--red); letter-spacing: 0.2px;
  }
  .hosts {
    position: absolute; left: 47px; top: 509px; width: 496px;
    display: flex; align-items: center; justify-content: space-between;
    font-family: "Fira Sans Condensed", sans-serif; font-weight: 300;
    font-size: 22px; color: var(--red); letter-spacing: 0.4px;
  }
</style>
</head>
<body>
<main class="canvas">

  <section class="card rsvp-card" aria-label="Response card">
    <svg class="outline-word" width="256" height="62" viewBox="0 0 256 62" aria-label="RSVP">
      <text x="4" y="58" font-size="72" textLength="220" lengthAdjust="spacingAndGlyphs">RSVP</text>
    </svg>
    <div class="rsvp-deadline">
      <p class="date-line">BY THE TWENTY FIRST OF AUGUST</p>
      <p class="year-line">TWO THOUSAND THIRTEEN</p>
    </div>
    <div class="rsvp-options">
      <div class="rsvp-option"><span class="rsvp-box"></span>ACCEPT</div>
      <div class="rsvp-option"><span class="rsvp-box"></span>REGRETS</div>
    </div>
    <div class="rsvp-names">
      <span>NAMES:</span>
      <svg width="146" height="8" viewBox="0 0 146 8" aria-hidden="true">
        <line x1="1" y1="4" x2="145" y2="4" stroke="#1a1a1a" stroke-width="1"/>
        <line x1="1" y1="1" x2="1" y2="7" stroke="#1a1a1a" stroke-width="1"/>
        <line x1="145" y1="1" x2="145" y2="7" stroke="#1a1a1a" stroke-width="1"/>
      </svg>
    </div>
  </section>

  <section class="card reception-card" aria-label="Reception card">
    <div class="reception-text reception-invite">
      <p>PLEASE JOIN US FOR</p>
      <p>LUNCH AND DANCING</p>
      <p class="lower">following the service</p>
    </div>
    <div class="reception-text reception-venue">
      <p class="venue-name">THE CORNER MILL</p>
      <p>880 Orchard Hill Road</p>
      <p>Ashby, VA 22190</p>
    </div>
    <svg class="outline-word" width="250" height="44" viewBox="0 0 250 44" aria-label="Celebrate">
      <text x="2" y="40" font-size="46" textLength="222" lengthAdjust="spacingAndGlyphs">CELEBRATE</text>
    </svg>
  </section>

  <section class="card invitation-card" aria-label="Invitation">
    <div class="intro">
      <p class="justify">IT IS WITH GREAT PRIDE AND JOY THAT</p>
      <p class="justify">WE INVITE YOU TO JOIN US AS OUR SON</p>
    </div>
    <svg class="outline-word" width="504" height="120" viewBox="0 0 504 120" aria-label="Ethan">
      <text x="1" y="114" font-size="138" textLength="500" lengthAdjust="spacingAndGlyphs">ETHAN</text>
    </svg>
    <p class="occasion justify">CELEBRATES HIS BAR MITZVAH</p>

    <div class="date-block">
      <p class="weekday justify">SATURDAY</p>
      <p class="small justify">SEPTEMBER TWENTY EIGHT</p>
      <p class="small justify">TWO THOUSAND THIRTEEN</p>
      <div class="time">
        <span class="time-num">10.30</span>
        <span class="time-note">IN THE<br>MORNING</span>
      </div>
    </div>

    <div class="venue-block">
      <p class="small justify">EASTERN RIDGE HEBREW</p>
      <p class="large justify">CONGREGATION</p>
      <p class="small justify gap">2270 LINDEN AVENUE FAIRMONT</p>
      <p class="large justify">VIRGINIA 20913</p>
    </div>

    <p class="kiddush justify">PLEASE JOIN US FOR KIDDUSH IMMEDIATELY FOLLOWING THE SERVICE</p>
    <div class="hosts">
      <svg width="92" height="8" viewBox="0 0 92 8" aria-hidden="true">
        <line x1="1" y1="4" x2="91" y2="4" stroke="#c8102e" stroke-width="1"/>
        <line x1="1" y1="1" x2="1" y2="7" stroke="#c8102e" stroke-width="1"/>
      </svg>
      <span>MARK AND MIRIAM KELLER</span>
      <svg width="100" height="8" viewBox="0 0 100 8" aria-hidden="true">
        <line x1="1" y1="4" x2="99" y2="4" stroke="#c8102e" stroke-width="1"/>
        <line x1="99" y1="1" x2="99" y2="7" stroke="#c8102e" stroke-width="1"/>
      </svg>
    </div>
  </section>

</main>
</body>
</html>
```